Home Refinance . Residential Mortgages

I want to post a small flyer as part of an email. I want do an email blast. I am a mortgage company and want to entice borrowers with my low interest rates. My website is www.oakmerecapital-demo.com
The colors must match the website colors.
VA IRRL REFINANCE.
30 YR. FIXED RATES as low as
2.25% | 2.437% APR
No Appraisal, No out of Pocket cost, NO Income Verification, NO Asset Verification, Close in 30 days or less

Target Market(s)

Real Estate agents & Borrowers looking to get a mortgage loan

Colors
0455a3
ec1f27
28a1d5

Requirements
Must have
• The colors must match the website colors.
OAKMERE CAPITAL, INC,.
4817B Wellsbury Road
Alexandria, VA 22987
QRLA 5830724
www.qrlaborrowerlookup-demo.com

Bright Harbor Pledge LOGO.

```html
<!DOCTYPE html>
<html lang="en">
<head>
<meta charset="utf-8">
<title>VA IRRL Refinance – Oakmere Capital</title>
<link href="https://fonts.googleapis.com/css2?family=Bebas+Neue&family=Quicksand:wght@400;500;600&display=swap" rel="stylesheet">
<style>
  :root{
    --page-bg:#f2f3f5;
    --card-bg:#ffffff;
    --navy-deep:#0a2360;
    --navy:#0b3275;
    --brand-blue:#0455a3;
    --sky:#28a1d5;
    --headline:#45c3fb;
    --ink:#2b2b2b;
    --white:#ffffff;
    --muted-white:rgba(255,255,255,.82);
    --photo-dark:#3a3f4a;
    --photo-light:#c9ccd1;
  }
  *{margin:0;padding:0;box-sizing:border-box;}
  html,body{width:1200px;height:857px;overflow:hidden;}
  body{background:var(--page-bg);position:relative;font-family:"Quicksand",sans-serif;}

  .flyer{
    position:absolute;left:75px;top:81px;width:1050px;height:696px;
    background:var(--card-bg);
    box-shadow:0 10px 40px rgba(20,30,60,.08);
    overflow:hidden;
  }
  .offer-panel{
    position:absolute;inset:0;
    background:linear-gradient(160deg,var(--navy-deep) 0%,var(--navy) 40%,#0e4f91 72%,#1e93cc 100%);
    clip-path:polygon(0 0,581px 0,519px 696px,0 696px);
  }
  .photo{
    position:absolute;left:0;top:91px;width:1050px;height:513px;
    background:linear-gradient(110deg,var(--photo-dark) 0%,#4b505a 45%,#a7a9ad 75%,var(--photo-light) 100%);
    clip-path:polygon(573px 0,1050px 0,1050px 513px,528px 513px);
  }
  .website{
    position:absolute;left:595px;width:440px;top:36px;
    text-align:center;white-space:nowrap;
    font-size:18px;font-weight:500;letter-spacing:2.4px;color:var(--ink);
  }
  .program{
    position:absolute;left:84px;top:109px;
    color:var(--white);font-size:25px;letter-spacing:2.6px;font-weight:400;
  }
  .headline{
    position:absolute;left:78px;top:183px;
    font-family:"Bebas Neue",sans-serif;font-size:98px;line-height:1;letter-spacing:1px;
    color:var(--headline);
  }
  .lead-in{
    position:absolute;left:79px;top:304px;
    color:var(--white);font-size:29px;letter-spacing:3.5px;
  }
  .rates{
    position:absolute;left:76px;top:378px;height:54px;
    display:flex;align-items:center;color:var(--white);font-size:40px;font-weight:500;letter-spacing:1px;
  }
  .rates .divider{width:2px;height:52px;background:var(--white);margin:0 32px 0 28px;}
  .benefits{
    position:absolute;left:78px;top:512px;list-style:none;
    color:var(--white);font-size:14px;letter-spacing:1.6px;line-height:28.5px;white-space:nowrap;
  }
  .benefits .closing{font-weight:600;letter-spacing:.6px;}
  .company-info{
    position:absolute;left:78px;top:618px;
    color:var(--muted-white);font-size:10px;letter-spacing:.8px;line-height:15px;white-space:nowrap;
  }
  .company-info .company-name{font-weight:600;color:var(--white);}
  .pledge{display:flex;align-items:center;gap:6px;}
  .pledge-mark{width:10px;height:10px;background:var(--white);}
  .cta{
    position:absolute;left:664px;top:619px;width:276px;height:61px;border-radius:31px;
    background:linear-gradient(90deg,var(--brand-blue) 0%,var(--sky) 60%,#22b9ee 100%);
    display:flex;align-items:center;justify-content:center;gap:18px;
    color:var(--white);font-size:22px;font-weight:500;letter-spacing:3px;text-decoration:none;
  }
  .cta svg{width:24px;height:26px;}
</style>
</head>
<body>
  <main class="flyer">
    <div class="offer-panel"></div>
    <div class="photo" role="img" aria-label="Photo of a loan officer in a suit holding up house keys over a desk with documents, a calculator and a small model house"></div>

    <p class="website">www.oakmerecapital-demo.com</p>

    <p class="program">VA IRRL REFINANCE</p>
    <h1 class="headline">FIXED RATES</h1>
    <p class="lead-in">as low as</p>
    <p class="rates"><span>2.25%</span><span class="divider"></span><span>2.437% APR</span></p>

    <ul class="benefits">
      <li>NO APPRAISAL, NO OUT OF POCKET COST,</li>
      <li>NO INCOME VERIFICATION, NO ASSET VERIFICATION,</li>
      <li class="closing">CLOSE IN 30 DAYS OR LESS</li>
    </ul>

    <address class="company-info">
      <div><span class="company-name">OAKMERE CAPITAL, INC,.</span> &nbsp;|&nbsp; QRLA 5830724</div>
      <div>4817B Wellsbury Road, Alexandria, VA 22987</div>
      <div>www.qrlaborrowerlookup-demo.com</div>
      <div class="pledge"><span class="pledge-mark" aria-hidden="true"></span><span>Bright Harbor Pledge</span></div>
    </address>

    <a class="cta" href="#">GET STARTED
      <svg viewBox="0 0 24 26" aria-hidden="true"><path d="M2 2l10 11-10 11M11 2l10 11-10 11" fill="none" stroke="#fff" stroke-width="2.2" stroke-linejoin="round"/></svg>
    </a>
  </main>
</body>
</html>
```